Animal Eye Clinic needs a Business card

We are a new veterinary ophthalmology practice (Tessaly Animal Eye Care) and we need a business card designed. We only see animal eyes - we are not a regular veterinary clinic. We already have a logo. We are looking for a professional, good looking business card to hand out to our clients. We are looking for something simple but professional and contemporary. Our logo is likely the only picture/graphic that needs to be on the card.
Updates

Contact Information for Business Card

Marisol Dunkley, BSc, DVM, MSc, DipACVO
Veterinary Ophthalmologist

Phone: 250.418.3097
Email: tessalyanimaleyecare@mailbrook.net
Website: tessalyanimaleyecare.net
Address: 1840 Pellworth Rd
Kelowna, BC, V4T 8M3

Colors

Designer to choose colors to be used in the design.

Requirements
Must have
• Our logo (attached)

```html
<!DOCTYPE html>
<html lang="en">
<head>
<meta charset="utf-8">
<title>Tessaly Animal Eye Care – Business Card</title>
<link rel="stylesheet" href="https://fonts.googleapis.com/css2?family=Roboto:wght@300;400;700&family=Roboto+Condensed:wght@700&display=swap">
<style>
  :root {
    --teal: #0a9aab;
    --teal-deep: #0a8c9c;
    --grey-text: #6b6b6b;
    --grey-rule: #8a8a8a;
    --paper: #f7f7f7;
    --white: #ffffff;
    --backdrop: #e6e8e9;
  }
  * { box-sizing: border-box; margin: 0; padding: 0; }
  html, body {
    width: 1200px; height: 864px; overflow: hidden;
    background: var(--backdrop);
    font-family: "Roboto", Arial, sans-serif;
  }
  .sheet {
    width: 1200px; height: 864px;
    display: flex; align-items: center; justify-content: center; gap: 40px;
  }
  .card {
    width: 540px; height: 309px; position: relative; overflow: hidden;
    box-shadow: 0 6px 18px rgba(0,0,0,0.18);
  }

  /* Front side */
  .card-front { background: var(--teal); color: var(--white); }
  .front-brand {
    position: absolute; left: 44px; top: 78px;
    display: flex; align-items: center; gap: 18px;
  }
  .brand-dot { width: 58px; height: 58px; border-radius: 50%; background: var(--white); flex: none; }
  .front-brand .brand-name {
    font-weight: 700; font-size: 31px; line-height: 1.1; letter-spacing: 0.5px; color: var(--white);
  }
  .front-web {
    position: absolute; left: 44px; bottom: 44px;
    font-family: "Roboto Condensed", Arial, sans-serif; font-weight: 700; font-size: 30px;
  }

  /* Back side */
  .card-back { background: var(--paper); }
  .back-brand {
    position: absolute; left: 36px; top: 28px;
    display: flex; align-items: center; gap: 12px;
  }
  .back-brand .brand-dot { width: 34px; height: 34px; background: var(--teal); }
  .back-brand .brand-name { font-weight: 700; font-size: 21px; color: var(--teal); letter-spacing: 0.3px; }

  .contact { position: absolute; left: 36px; top: 92px; }
  .person-name { font-weight: 400; font-size: 19px; color: var(--grey-text); text-transform: uppercase; letter-spacing: 0.3px; }
  .credentials { color: var(--teal); text-transform: none; }
  .person-title { font-weight: 400; font-size: 15px; color: var(--teal); margin-top: 2px; }
  .detail-list { list-style: none; margin-top: 12px; }
  .detail {
    display: flex; align-items: center; gap: 9px;
    font-size: 14.5px; font-weight: 400; color: var(--grey-text); line-height: 24px;
  }
  .detail-icon { width: 16px; height: 16px; flex: none; }
  .detail-address { padding-left: 0; }

  .band-rule { position: absolute; left: 0; right: 0; bottom: 46px; height: 4px; background: var(--grey-rule); }
  .band {
    position: absolute; left: 0; right: 0; bottom: 0; height: 40px; background: var(--teal);
    display: flex; align-items: center; justify-content: flex-end; padding-right: 28px;
  }
  .band-web { font-family: "Roboto Condensed", Arial, sans-serif; font-weight: 700; font-size: 21px; color: var(--white); }
</style>
</head>
<body>
<main class="sheet">

  <section class="card card-front" aria-label="Card front">
    <div class="front-brand">
      <span class="brand-dot"></span>
      <span class="brand-name">Tessaly Animal Eye Care</span>
    </div>
    <p class="front-web">tessalyanimaleyecare.net</p>
  </section>

  <section class="card card-back" aria-label="Card back">
    <div class="back-brand">
      <span class="brand-dot"></span>
      <span class="brand-name">Tessaly Animal Eye Care</span>
    </div>

    <div class="contact">
      <p class="person-name">Marisol Dunkley, <span class="credentials">BSc, DVM, MSc, DipACVO</span></p>
      <p class="person-title">Veterinary Ophthalmologist</p>
      <ul class="detail-list">
        <li class="detail">
          <svg class="detail-icon" viewBox="0 0 16 16" aria-hidden="true">
            <rect width="16" height="16" rx="2" fill="var(--teal)"/>
            <rect x="5" y="3" width="6" height="10" rx="1" fill="none" stroke="#fff" stroke-width="1.3"/>
          </svg>
          250.418.3097
        </li>
        <li class="detail">
          <svg class="detail-icon" viewBox="0 0 16 16" aria-hidden="true">
            <rect width="16" height="16" rx="2" fill="var(--teal)"/>
            <rect x="3" y="4.5" width="10" height="7" fill="none" stroke="#fff" stroke-width="1.2"/>
            <path d="M3 4.5 L8 8.5 L13 4.5" fill="none" stroke="#fff" stroke-width="1.2"/>
          </svg>
          tessalyanimaleyecare@mailbrook.net
        </li>
        <li class="detail detail-address">1840 Pellworth Rd, Kelowna, BC, V4T 8M3</li>
      </ul>
    </div>

    <div class="band-rule"></div>
    <div class="band"><span class="band-web">tessalyanimaleyecare.net</span></div>
  </section>

</main>
</body>
</html>
```